Epoxy Flooring Contractor business card

We need a business card to promote a new addition to our business. We now offer Epoxy Flooring. We would like for the business card to include the images attached. One is our logo, the other is a sample of metallic epoxy flooring, we would like to incorporate that somewhere into the design. I was thinking an icon of a man pushing a concrete grinder and have the color set to the metallic epoxy color. I found a business card sample on this website, I will attach it. It has the icon that we are looking for, or something similar.
Our company name is Harborline Coatings LLC
Our owners name is Dane Morrow
Phone is 561-482-7160
website is www.harborline-coatingsllc.example
please let me know if you need any other info

Contact Information for Business Card

Harborline Coatings LLC
Dane Morrow, owner
Phone: 561-482-7160
Address: P.O Box 8241 Lake Worth, FL 33467
www.Harborline-CoatingsLLC.example
HarborlineCoatingsLLC@mailbox.example
Include logo attached
It must include a Clip art of man with concrete grinder
Must include metallic epoxy design attached
Must include the following text
Residential Garage Flooring
Epoxy Countertops
Commercial Epoxy Flooring
Restaurant Flooring
Warehouse Flooring
Licensed & Insured
Free Estimates

Colors

Designer to choose colors to be used in the design.

Requirements
Must have
• Include logo attached
• It must include a Clip art of man with concrete grinder
• Must include metallic epoxy design attached
• Must include the following text
• Garage Epoxy Flooring
• Residential Epoxy Flooring
• Concrete Floor Crack Repairs
• Concrete Floor Grinding
• Commercial & Warehouse Epoxy Flooring
• Restaurant Epoxy Flooring
• Epoxy Countertops
• Non Slip Epoxy Pool Decks
• Textured Finishes, Flakes, Granite Coat, Metallic & Quartz
• FREE ESTIMATES • LICENSED & INSURED

```html
<!DOCTYPE html>
<html lang="en">
<head>
<meta charset="utf-8">
<title>Harborline Coatings – Business Card</title>
<link href="https://fonts.googleapis.com/css2?family=Montserrat:wght@500;600&family=Source+Sans+3:wght@400;600&display=swap" rel="stylesheet">
<style>
  :root{
    --stage:#d9dbde;
    --card-white:#ffffff;
    --band-blue:#41608a;
    --name-blue:#9cb9e4;
    --logo-blue:#4a6690;
    --footer-text:#45608a;
    --steel-dark:#5d6670;
    --steel-mid:#8d959e;
    --steel-light:#c4c9ce;
    --epoxy-deep:#274a78;
    --epoxy-light:#8fb1d6;
    --white:#ffffff;
  }
  *{box-sizing:border-box;margin:0;padding:0}
  html,body{width:1200px;height:800px;overflow:hidden}
  body{background:var(--stage);font-family:"Source Sans 3",Arial,sans-serif;position:relative}

  .card{position:absolute;left:290px;width:620px;height:354px;overflow:hidden;box-shadow:0 6px 18px rgba(0,0,0,.18)}
  .card--services{top:26px}
  .card--contact{top:416px;background:var(--card-white)}

  /* services side */
  .services__backdrop{position:absolute;inset:0;
    background:
      linear-gradient(180deg,var(--steel-dark) 0%,var(--steel-mid) 40%,var(--steel-light) 62%,var(--steel-mid) 100%);}
  .services__worker{position:absolute;left:40px;top:40px;width:190px;height:290px;border-radius:6px;
    background:linear-gradient(180deg,rgba(255,255,255,.85),rgba(255,255,255,.55));}
  .services__brand{position:absolute;left:250px;top:86px;right:24px;text-align:right;
    font-family:"Montserrat",Arial,sans-serif;font-weight:600;color:var(--white);font-size:30px;letter-spacing:3px;line-height:1.05}
  .services__list{position:absolute;left:238px;right:18px;top:178px;text-align:center;color:var(--white);
    font-size:14.5px;line-height:1.32;text-shadow:0 1px 2px rgba(0,0,0,.35)}

  /* contact side */
  .contact__brand{position:absolute;left:40px;top:30px;display:flex;align-items:center;gap:14px;
    font-family:"Montserrat",Arial,sans-serif;font-weight:600;color:var(--logo-blue);font-size:30px;letter-spacing:3px;line-height:1.05}
  .contact__brand-mark{width:26px;height:26px;background:var(--logo-blue)}
  .contact__band{position:absolute;left:0;right:0;top:118px;height:176px;background:var(--band-blue)}
  .contact__photo{position:absolute;right:0;top:150px;width:250px;height:144px;
    background:linear-gradient(90deg,rgba(65,96,138,0) 0%,var(--epoxy-deep) 30%,var(--epoxy-light) 75%,var(--epoxy-deep) 100%)}
  .contact__person{position:absolute;left:78px;top:136px}
  .contact__name{font-size:22px;font-weight:600;color:var(--name-blue);text-transform:uppercase;letter-spacing:.5px}
  .contact__role{font-size:14px;color:var(--white);text-transform:uppercase;margin-top:-2px}
  .contact__list{position:absolute;left:62px;top:200px;list-style:none;color:var(--white);font-size:16px;line-height:1.38}
  .contact__list li{display:flex;align-items:center;gap:9px}
  .contact__list svg{width:14px;height:14px;flex:none}
  .contact__footer{position:absolute;left:40px;top:308px;color:var(--footer-text);font-size:16.5px}
</style>
</head>
<body>

<section class="card card--services">
  <div class="services__backdrop" role="img" aria-label="Photo of a warehouse interior with a speckled epoxy flake floor"></div>
  <div class="services__worker" role="img" aria-label="Illustration of a worker pushing a concrete grinder"></div>
  <div class="services__brand">Harborline<br>Coatings</div>
  <p class="services__list">
    Garage Epoxy Flooring • Residential Epoxy Flooring<br>
    Concrete Floor Crack Repairs • Concrete Floor Grinding<br>
    Textured Finishes, Flakes, Granite Coat, Metallic &amp; Quartz<br>
    Commercial &amp; Warehouse Epoxy Flooring<br>
    Epoxy Countertops • Restaurant Epoxy Flooring<br>
    Non Slip Epoxy Pool Decks<br>
    FREE ESTIMATES • LICENSED &amp; INSURED
  </p>
</section>

<section class="card card--contact">
  <div class="contact__brand"><span class="contact__brand-mark"></span><span>Harborline<br>Coatings</span></div>
  <div class="contact__band"></div>
  <div class="contact__photo" role="img" aria-label="Metallic blue epoxy floor sample with a worker pushing a concrete grinder"></div>
  <div class="contact__person">
    <p class="contact__name">Dane Morrow</p>
    <p class="contact__role">Owner</p>
  </div>
  <ul class="contact__list">
    <li><svg viewBox="0 0 16 16" aria-hidden="true"><path fill="#fff" d="M3.6 1.2l2.3 2.6-1.3 1.6c.9 2.1 2.3 3.6 4.4 4.6l1.6-1.3 2.6 2.3-1.5 2.3C7.2 12.9 3.1 8.8 1.7 2.7z"/></svg>561-482-7160</li>
    <li><svg viewBox="0 0 16 16" aria-hidden="true"><rect x="1" y="3" width="14" height="10" fill="none" stroke="#fff" stroke-width="1.4"/><path d="M1 3l7 6 7-6" fill="none" stroke="#fff" stroke-width="1.4"/></svg>HarborlineCoatingsLLC@mailbox.example</li>
    <li><svg viewBox="0 0 16 16" aria-hidden="true"><circle cx="8" cy="8" r="6.5" fill="none" stroke="#fff" stroke-width="1.3"/><ellipse cx="8" cy="8" rx="2.8" ry="6.5" fill="none" stroke="#fff" stroke-width="1.1"/><path d="M1.5 8h13" stroke="#fff" stroke-width="1.1"/></svg>www.Harborline-CoatingsLLC.example</li>
  </ul>
  <p class="contact__footer">Harborline Coatings LLC | P.O Box 8241 Lake Worth, FL 33467</p>
</section>

</body>
</html>
```